Pediatric Pelvic Health Brochure

Looking to design a brochure for Marlow Brook's pelvic health program. I can provide imagery once I see the layout. Our website is marlowbrookpt.example so the look should reflect that

If you see PDF titled blue and word doc you will see what we provided as thoguhts.

Target Market(s)

parents of children

Industry/Entity Type

Health And Wellness

Font styles to use
Serif

Requirements
Must have
• clear call outs - easy to read with copy,
Should not have
• not look bland or dated

```html
<!DOCTYPE html>
<html lang="en">
<head>
<meta charset="utf-8">
<title>Marlow Brook – Pediatric Pelvic Health Brochure</title>
<link href="https://fonts.googleapis.com/css2?family=Raleway:ital,wght@0,400;0,500;0,700;0,800;1,500&display=swap" rel="stylesheet">
<style>
:root{
  --navy:#1b3f95;
  --navy-deep:#16347f;
  --royal:#2153b5;
  --cyan:#12aee8;
  --cyan-light:#3cc3f2;
  --ink:#333a45;
  --white:#ffffff;
  --backdrop:#7a7a7a;
}
*{margin:0;padding:0;box-sizing:border-box}
html,body{width:917px;height:1200px;overflow:hidden;background:var(--backdrop)}
body{position:relative;font-family:"Raleway",sans-serif;color:var(--ink)}
.sheet{position:absolute;left:117px;width:680px;height:511px;display:flex;background:var(--white)}
.sheet--outside{top:54px}
.sheet--inside{top:615px}
.panel{position:relative;width:226.67px;height:100%;overflow:hidden}
.photo{position:absolute;left:0;top:0;width:100%}

/* outside: diagnoses */
.diagnoses .photo{height:160px;background:linear-gradient(160deg,#ecebea,#d9d6d6 55%,#b9a9c9)}
.diagnoses .wave{position:absolute;left:0;top:140px}
.diagnoses h2{position:absolute;left:28px;top:161px;font-size:13px;font-weight:800;color:var(--navy);line-height:15.5px}
.checklist{position:absolute;left:28px;top:198px;width:190px;list-style:none;font-size:9.6px;line-height:13.6px;color:var(--ink)}
.checklist li{position:relative;padding-left:14px}
.checklist li::before{content:"";position:absolute;left:0;top:3px;width:7px;height:7px;background:var(--navy)}
.checklist li::after{content:"";position:absolute;left:1.5px;top:4px;width:3px;height:4px;border:solid #fff;border-width:0 1.3px 1.3px 0;transform:rotate(40deg)}

/* outside: contact */
.contact{background:linear-gradient(180deg,var(--navy-deep),var(--royal));color:var(--white);text-align:center}
.contact .brand-name{position:absolute;left:0;right:0;top:100px;font-size:15px;font-weight:500}
.contact h2{position:absolute;left:0;right:0;top:176px;font-size:13.5px;font-weight:700;letter-spacing:.3px}
.contact .rule{position:absolute;left:103px;width:20px;height:1px;background:rgba(255,255,255,.7)}
.contact address{position:absolute;left:0;right:0;top:210px;font-style:normal;font-size:11px;line-height:13.8px}
.contact .lines{position:absolute;left:0;right:0;top:270px;font-size:11px;line-height:13.8px}
.contact .wave{position:absolute;left:0;top:360px}
.contact .offer{position:absolute;left:34px;right:34px;top:430px;font-size:11px;line-height:13.8px}

/* outside: cover */
.cover .brand{position:absolute;left:0;right:0;top:26px;text-align:center;font-size:20px;font-weight:500;color:var(--navy)}
.cover .photo{top:82px;height:320px;background:linear-gradient(160deg,#2b6fc8,#4bb3ec 50%,#1f9ae0)}
.cover .band{position:absolute;left:0;top:0}
.cover h1{position:absolute;left:0;right:0;top:372px;text-align:center;font-size:22px;font-weight:800;line-height:24.5px;color:var(--navy)}
.cover .tagline{position:absolute;left:0;right:0;top:424px;text-align:center;font-size:14.5px;font-style:italic;font-weight:500;line-height:18px;color:var(--white)}
.cover .site-btn{position:absolute;left:34px;top:471px;width:152px;height:25px;background:var(--navy);color:var(--white);font-size:11.5px;font-weight:700;text-align:center;line-height:25px;letter-spacing:.3px}

/* inside */
.inside-photo{height:134px}
.ribbon{position:absolute;left:0;width:100%;height:36px;background:var(--cyan);color:var(--white);font-size:17px;font-weight:800;text-align:center;line-height:36px}
.help .photo,.partner .photo{background:linear-gradient(140deg,#c9c4c0,#e9e6e4 55%,#b9b2ae)}
.partner .photo{background:linear-gradient(140deg,#d9c8c2,#e7d9da 45%,#3b74c9)}
.help .ribbon,.partner .ribbon{top:134px}
.copy{position:absolute;font-size:10px;line-height:13.6px;text-align:justify;color:var(--ink)}
.copy p+p{margin-top:13.6px}
.help{background:linear-gradient(90deg,#fff 70%,#ececec)}
.help .copy{left:17px;right:23px;top:190px}
.partner{background:linear-gradient(90deg,#ececec,#fff 25%)}
.partner .copy{left:16px;right:18px;top:189px;text-align:left}

.specialize{background:linear-gradient(180deg,var(--navy),#2048a3 60%,#1b3f95)}
.specialize .ribbon{top:0;height:35px;line-height:35px}
.specialize .copy{left:19px;right:20px;top:73px;color:var(--white)}
.specialize .brand-name{position:absolute;left:0;right:0;top:374px;text-align:center;font-size:22px;font-weight:500;color:var(--white)}
.specialize .call{position:absolute;left:0;right:0;top:422px;text-align:center;font-size:18px;font-weight:800;color:var(--cyan-light)}
.specialize .web{position:absolute;left:0;right:0;top:445px;text-align:center;font-size:15.5px;font-weight:800;color:var(--white)}

.quote{position:absolute;left:18px;top:399px;width:190px;height:92px;border:1px solid var(--navy);padding:20px 14px 0;text-align:center}
.quote .mark{position:absolute;left:83px;top:-11px;width:22px;height:22px;border-radius:50%;background:var(--cyan);border:3px solid #fff}
.quote p{font-size:7.2px;line-height:9.2px;color:var(--ink)}
.quote cite{display:block;margin-top:8px;font-size:7.2px;font-style:normal;color:var(--cyan)}
</style>
</head>
<body>

<section class="sheet sheet--outside">
  <div class="panel diagnoses">
    <div class="photo" role="img" aria-label="Therapist guiding a young girl through a bridge exercise on a treatment table"></div>
    <svg class="wave" width="227" height="40" viewBox="0 0 227 40">
      <path d="M0 22 Q110 -6 227 6 L227 40 L0 40Z" fill="var(--cyan)"/>
      <path d="M0 28 Q110 2 227 14 L227 40 L0 40Z" fill="var(--white)"/>
    </svg>
    <h2>WE TREAT<br>ARANGE OF DIAGNOSES</h2>
    <ul class="checklist">
      <li>Constipation</li>
      <li>Increased urinary frequency</li>
      <li>Decreased urinary frequency</li>
      <li>Day-time incontinence</li>
      <li>Night-time incontinence,</li>
      <li>bed-wetting, or enuresis</li>
      <li>Giggle incontinence</li>
      <li>Incontinence in the athletic<br>female child or teenager</li>
      <li>Waking up in the night to<br>urinate or nocturia</li>
      <li>Difficulty with urination: straining, slow flow, pain during or after urination</li>
      <li>Reduced sensation of bladder or bowel fullness</li>
      <li>Pain in the abdomen, bladder or lower back</li>
      <li>Fecal incontinence</li>
      <li>Treatment after pediatric pelvic Surgeries</li>
    </ul>
  </div>

  <div class="panel contact">
    <div class="brand-name">Marlow Brook</div>
    <h2>CONTACT US</h2>
    <div class="rule" style="top:200px"></div>
    <address>48 Harbor Lane<br>Ground Floor<br>Westfield, NY 10990</address>
    <div class="rule" style="top:262px"></div>
    <div class="lines">555.014.2200<br>Marlowbrookpt.example</div>
    <svg class="wave" width="227" height="151" viewBox="0 0 227 151">
      <path d="M0 70 Q90 10 227 5 L227 151 L0 151Z" fill="var(--white)" opacity=".85"/>
      <path d="M0 78 Q90 18 227 12 L227 151 L0 151Z" fill="var(--cyan)"/>
    </svg>
    <p class="offer">We offer a FREE 15 minute consultation to help you determine if physical therapy is right for you and your child or teen..</p>
  </div>

  <div class="panel cover">
    <div class="brand">Marlow Brook</div>
    <div class="photo" role="img" aria-label="Therapist working with a girl on an exercise ball in a bright gym"></div>
    <svg class="band" width="227" height="511" viewBox="0 0 227 511">
      <path d="M0 382 Q140 370 227 240 L227 511 L0 511Z" fill="var(--cyan)"/>
    </svg>
    <h1>PEDIATRIC<br>PELVIC HEALTH</h1>
    <p class="tagline">Treat ing Infants, Children<br>&amp; Adolescents</p>
    <div class="site-btn">MARLOWBROOKPT.EXAMPLE</div>
  </div>
</section>

<section class="sheet sheet--inside">
  <div class="panel help">
    <div class="photo inside-photo" role="img" aria-label="Parent on a video call with a therapist on a laptop"></div>
    <div class="ribbon">WE HELP</div>
    <div class="copy">
      <p>Although millions of children suffer from pelvic floor dysfunction, it often takes a long time to receive the right treatment.</p>
      <p>Typically, children are toilet trained by age 4. After age 4, bowel and bladder dysfunction is considered a a major medical issue that affects the family unit.</p>
      <p>Pelvic problems in children greatly influence the quality of life, self-image, social interactions, participation in sports, etc. A pelvic physical therapist can help restore normality in bladder and bowel function and prevent the progression of problems that, if untreated, may be carried over into adult life.</p>
    </div>
  </div>

  <div class="panel specialize">
    <div class="ribbon">WE SPECIALIZE</div>
    <div class="copy">
      <p>All pelvic physical therapy treatments are always done with a physical therapist trained in pediatric pelvic floor issues, and always with your doctor's knowledge. Children are dressed and parents and guardians are present.</p>
      <p>During each session, your child or teen will work exclusively with one of our pelvic health physical therapists to help build strength, improve movement, and strengthen the skills and confidence needed to complete daily activities.</p>
    </div>
    <div class="brand-name">Marlow Brook</div>
    <div class="call">Call Us 555.014.2200</div>
    <div class="web">MARLOWBROOKPT.EXAMPLE</div>
  </div>

  <div class="panel partner">
    <div class="photo inside-photo" role="img" aria-label="Therapist supporting a child lying back over a blue exercise ball"></div>
    <div class="ribbon">WE PARTNER</div>
    <div class="copy">
      <p>Children or teens with Pelvic dysfunction, and those with neurological pathologies have different needs than adults. Thus our therapists needs to work with parents, teachers, and other healthcare professionals such as urologists, GI's, pediatric physical therapists, and psychologists to provide an integrated and comprehensive plan of care.</p>
    </div>
    <div class="quote">
      <span class="mark"></span>
      <p>Our daughter gained so much confidence. The team was patient, kind, and always explained each step to us clearly. We felt supported at every visit.</p>
      <cite>Dana R.</cite>
    </div>
  </div>
</section>

</body>
</html>
```